Aircraft maintenance buisness card

I am an aircraft mechanic looking for a personal buisness card . I would like my name and a title of Aircraft Maintenance Manager . I would like a suttle picture of an aircraft and helicopter .

elegant and professional wtih my contact .

My name should be on the car and Aircraft Maintenance Manager under with my contact infor below .

i have attached some pictures but i am open to other pics and ideas . I would like a airliner or private jet and a helicopter in the picture . The Images should be suttle and not the main idea . I also uploaded a picture of a jet engine which is cool . Be creative and i will work with you to finalize something .
Updates

Project Deadline Extended
Reason: Looking for more variations . Very good so far but looiking for a bit more styles and i uploaded my logo that i purchased . Please use my logo and be creative with it . I like some variations of black card with maybe some pictures that i uploaded but i am open to ideas . Be creative and i will work with you .

Project Deadline Extended
Reason: Looking for more designs and variations . Not yet satisfied with the designs i have gotten .

Industry/Entity Type

Aviation

Contact Information for Business Card

Aircraft Maintenance Manager

Font styles to use
Serif

Colors

Designer to choose colors to be used in the design.

Requirements
Must have
• An aviation related Logo if possible incorporated in the card possibly
• My name
• Tiberio Malvade Furtunato
• 482 Pellow St.
• Dunmere , WR
• 08519
• Email: Lwskyfixtech@mailvora.com
Nice to have
• Suttle Backround of a Private Jet or Airliner and a Helicopter .

```html
<!DOCTYPE html>
<html lang="en">
<head>
<meta charset="utf-8">
<title>Pellow Aero – Business Card</title>
<link href="https://fonts.googleapis.com/css2?family=Roboto:wght@400;500&display=swap" rel="stylesheet">
<style>
  :root {
    --backdrop: #8f9094;
    --card-white: #ffffff;
    --card-black: #231f20;
    --brand-blue: #1f47a3;
    --brand-blue-dark: #14306f;
    --title-blue: #9db3ee;
    --ink: #1e1e1e;
  }
  * { box-sizing: border-box; margin: 0; padding: 0; }
  html, body { width: 1200px; height: 1078px; overflow: hidden; }
  body {
    background: var(--backdrop);
    font-family: "Roboto", Arial, sans-serif;
    position: relative;
  }
  .card {
    position: absolute;
    left: 216px;
    width: 768px;
    height: 460px;
    background: var(--card-white);
    overflow: hidden;
  }
  .card--front { top: 49px; }
  .card--back { top: 569px; }

  /* Front */
  .front-brand {
    position: absolute; left: 0; top: 0; width: 100%; height: 200px;
    display: flex; align-items: center; justify-content: center; gap: 16px;
  }
  .brand-dot {
    width: 46px; height: 46px; border-radius: 50%; background: var(--brand-blue);
  }
  .brand-name {
    font-weight: 500; font-size: 40px; letter-spacing: 2px;
    color: var(--brand-blue); text-transform: uppercase;
  }
  .front-stripe {
    position: absolute; left: 0; top: 200px; width: 100%; height: 8px;
    background: var(--brand-blue);
  }
  .front-photo {
    position: absolute; left: 0; top: 208px; width: 100%; height: 252px;
    background: linear-gradient(100deg, #b94a45 0%, #8fa4b8 28%, #dfe6ee 45%, #9fb7d3 62%, #6c7f94 80%, #2f5ca8 100%);
  }

  /* Back */
  .back-dark {
    position: absolute; left: 412px; top: 0; width: 356px; height: 100%;
    background: var(--card-black);
  }
  .back-brand {
    position: absolute; left: 0; top: 70px; width: 412px;
    display: flex; align-items: center; justify-content: center; gap: 14px;
  }
  .back-brand .brand-name { font-size: 34px; }
  .back-brand .brand-dot { width: 38px; height: 38px; }
  .contact-list {
    position: absolute; left: 92px; top: 300px; list-style: none;
  }
  .contact-list li {
    display: flex; align-items: center; gap: 10px;
    font-size: 17px; color: var(--ink); margin-bottom: 12px;
  }
  .contact-icon { width: 18px; height: 18px; flex: none; }
  .name-banner {
    position: absolute; left: 396px; top: 140px; width: 372px; height: 96px;
    background: var(--brand-blue);
    padding: 18px 0 0 40px;
  }
  .name-fold {
    position: absolute; left: 396px; top: 236px; width: 26px; height: 16px;
  }
  .holder-name { font-size: 26px; font-weight: 500; color: #fff; }
  .holder-title { font-size: 17px; color: var(--title-blue); margin-top: 6px; }
  .address {
    position: absolute; left: 412px; top: 300px; width: 356px;
    text-align: center; font-size: 17px; line-height: 1.45; color: #fff;
  }
</style>
</head>
<body>
  <section class="card card--front">
    <div class="front-brand">
      <span class="brand-dot"></span>
      <span class="brand-name">Pellow Aero</span>
    </div>
    <div class="front-stripe"></div>
    <div class="front-photo" role="img" aria-label="Collage of aircraft photos: a red helicopter, an airliner in flight, a private jet among clouds and a blue rescue helicopter"></div>
  </section>

  <section class="card card--back">
    <div class="back-dark"></div>
    <div class="back-brand">
      <span class="brand-dot"></span>
      <span class="brand-name">Pellow Aero</span>
    </div>
    <ul class="contact-list">
      <li>
        <svg class="contact-icon" viewBox="0 0 18 18"><rect width="18" height="18" rx="2" fill="var(--brand-blue)"/><path d="M4 6h10v7H4z M4 6l5 4 5-4" fill="none" stroke="#fff" stroke-width="1.3"/></svg>
        tiberio@pellowaeroservices.com
      </li>
      <li>
        <svg class="contact-icon" viewBox="0 0 18 18"><rect width="18" height="18" rx="2" fill="var(--brand-blue)"/><circle cx="9" cy="9" r="5" fill="none" stroke="#fff" stroke-width="1.3"/><path d="M4 9h10M9 4c-2.5 3-2.5 7 0 10M9 4c2.5 3 2.5 7 0 10" fill="none" stroke="#fff" stroke-width="1"/></svg>
        pellowaeroservices.com
      </li>
    </ul>
    <div class="name-banner">
      <p class="holder-name">Tiberio Malvade Furtunato</p>
      <p class="holder-title">Aircraft Maintenance Manager</p>
    </div>
    <svg class="name-fold" viewBox="0 0 26 16"><polygon points="0,0 26,0 26,16" fill="var(--brand-blue-dark)"/></svg>
    <p class="address">482 Pellow St.<br>Dunmere , WR, 08519</p>
  </section>
</body>
</html>
```